Modernising a Traditional Image - Velmar Brass Band

The Brass Band musical world in Britain is under threat. It is a wonderful place for children and amateurs to learn a musical instrument - it is our responsibility to protect it and grow it.
We can have a combined image of being old and slow. Our organisation wants to celebrate youth and a new / innovative way of doing things.

We don't wish to create a new logo as that exists now on our rather expensive uniforms - BUT to provide an attractive message for potential young players, something that we can use on Roll-up Banners, Facebook posts, Web banners, Tickets, Concert programmes. In short a cohesive image for our communication. I have however included the Logo design - so perhaps preparing the road for a future logo transition, or perhaps for use with the Velmar Academy / Training Band.

UPDATE TO BRIEF 26/08 - DO NOT PLEASE INCLUDE THE OLD LOGO AT ALL. THINK NEW, THINK BOLD, THINK BRIGHT, YOUNG, ETC.

The final designs need to communicate a basis of tradition, but a bright, young innovative future. Please consider the bright brass bands in UK (https://www.instagram.com/qrtwlx/), and those in the Netherlands, Scandinavia, etc.

Current website / socials:
https://www.facebook.com/Velmarband
https://www.facebook.com/NorthGlimwick
https://www.velmar-example.band/

Target Market(s)

Young learners of musical instrument. Followers of music events, theatre, et.

Industry/Entity Type

Music theatre education

Requirements
Must have
• An invite.. 'come witness the magic being made at Band Practice Thursdays'.. as an example
Nice to have
• Bright colour (not linked to current logo). Surprise me
Should not have
• Any link to old logo

```html
<!DOCTYPE html>
<html lang="en">
<head>
<meta charset="utf-8">
<title>Velmar Band – Band Practice Thursdays</title>
<link rel="stylesheet" href="https://fonts.googleapis.com/css2?family=Anton&family=Montserrat:wght@700;800&display=swap">
<style>
  :root {
    --backdrop: #f4cdd3;
    --purple-deep: #4f1794;
    --purple: #6a1fa6;
    --magenta: #c0248e;
    --hot-pink: #ff3f8e;
    --salmon: #fb8c92;
    --blush: #ffe3e8;
  }
  html, body {
    margin: 0;
    width: 1200px;
    height: 685px;
    overflow: hidden;
    background: var(--backdrop);
  }
  .stage {
    position: relative;
    width: 1200px;
    height: 685px;
  }
  .poster {
    position: absolute;
    left: 343px;
    top: 0;
    width: 513px;
    height: 685px;
    display: block;
  }
  .headline {
    font-family: "Anton", "Impact", sans-serif;
    fill: var(--salmon);
  }
  .invite, .address, .footer-text {
    font-family: "Montserrat", "Arial", sans-serif;
    font-weight: 800;
    fill: var(--blush);
    letter-spacing: 0.06em;
  }
  .footer-text { font-weight: 700; letter-spacing: 0.03em; }
  .frame, .diagonal, .footer-box { fill: none; stroke: var(--salmon); }
  .divider { stroke: var(--blush); stroke-dasharray: 3 2.5; stroke-width: 0.8; }
  .social-dot { fill: var(--blush); }
</style>
</head>
<body>
<main class="stage">
  <svg class="poster" viewBox="0 0 513 685" xmlns="http://www.w3.org/2000/svg" role="img" aria-label="Velmar Band poster: You love music? So do we! Come witness the wonder of music at our band practice on Thursdays">
    <defs>
      <linearGradient id="poster-base" x1="0" y1="0" x2="1" y2="1">
        <stop offset="0" stop-color="var(--purple)"/>
        <stop offset="0.5" stop-color="var(--magenta)"/>
        <stop offset="1" stop-color="var(--purple-deep)"/>
      </linearGradient>
      <radialGradient id="glow-top-right" cx="1" cy="0" r="0.7">
        <stop offset="0" stop-color="var(--hot-pink)"/>
        <stop offset="1" stop-color="var(--hot-pink)" stop-opacity="0"/>
      </radialGradient>
      <radialGradient id="glow-bottom-left" cx="0" cy="0.72" r="0.55">
        <stop offset="0" stop-color="var(--hot-pink)"/>
        <stop offset="1" stop-color="var(--hot-pink)" stop-opacity="0"/>
      </radialGradient>
    </defs>

    <g class="background">
      <rect width="513" height="685" fill="url(#poster-base)"/>
      <rect width="513" height="685" fill="url(#glow-top-right)"/>
      <rect width="513" height="685" fill="url(#glow-bottom-left)"/>
      <rect x="1" y="0" width="511" height="685" fill="none" stroke="var(--salmon)" stroke-width="3"/>
    </g>

    <rect class="frame" x="21" y="29" width="472" height="627" stroke-width="1.3"/>

    <g class="diagonals" stroke-width="1.3">
      <line class="diagonal" x1="104" y1="474" x2="455" y2="51"/>
      <line class="diagonal" x1="140" y1="440" x2="437" y2="80"/>
      <line class="diagonal" x1="180" y1="412" x2="416" y2="84"/>
    </g>

    <g class="headline">
      <text x="61" y="205" font-size="178" textLength="228" lengthAdjust="spacingAndGlyphs">YOU</text>
      <text x="59" y="299" font-size="118" textLength="166" lengthAdjust="spacingAndGlyphs">LOVE</text>
      <text x="58" y="362" font-size="52" textLength="114" lengthAdjust="spacingAndGlyphs">MUSIC ?</text>
      <text x="390" y="195" font-size="58" textLength="55" lengthAdjust="spacingAndGlyphs">SO</text>
      <text x="343" y="299" font-size="118" textLength="102" lengthAdjust="spacingAndGlyphs">DO</text>
      <text x="256" y="449" font-size="156" textLength="189" lengthAdjust="spacingAndGlyphs">WE!</text>
    </g>

    <g class="invite" font-size="11.5" text-anchor="middle">
      <text x="255" y="500">COME WITNESS THE WONDER OF MUSIC AT</text>
      <text x="255" y="516">OUR BAND PRACTICE ON THURSDAYS</text>
    </g>
    <line class="divider" x1="64" y1="523" x2="450" y2="523"/>

    <g class="address" font-size="11.5" text-anchor="middle">
      <text x="255" y="542">VELMAR BAND,</text>
      <text x="255" y="559">NORTH GLIMWICK COMMUNITY CENTRE,</text>
      <text x="255" y="576">FERROW MEADOW, NORTH GLIMWICK</text>
      <text x="255" y="593">DUNMERE,</text>
      <text x="255" y="610">QX9 2LB</text>
    </g>

    <rect class="footer-box" x="54" y="622" width="406" height="34" stroke-width="1.3"/>
    <g class="footer-text" font-size="10">
      <text x="68" y="643">www.velmar-example.band</text>
      <circle class="social-dot" cx="232" cy="639.5" r="5"/>
      <text x="242" y="643">Velmarband | NorthGlimwick</text>
    </g>
  </svg>
</main>
</body>
</html>
```